Business Card Design

IT Solutions company.

I need a professional looking design with my company logo if possible.

Logo is located here:
http://www.brivelsystems.co.uk/dev/images/logo1.jpg
Feel free to redesign the logo if you think you have any better suggestions.

Our services include, IT Infrastructure/Telephony Maintenance & Hosting Services. Kernix and Panora Solutions, App Development.

Out website is currently under development:
http://www.brivelsystems.co.uk/dev/

I'm looking for a colourful but professional looking business card.

Industry/Entity Type

Business

Contact Information for Business Card

Brivel Systems Group Ltd
Morven Halsey
07845193870
www.brivelsystems.co.uk
mhalsey@brivelsystems.co.uk

```html
<!DOCTYPE html>
<html lang="en">
<head>
<meta charset="UTF-8">
<title>Brivel Systems Group Ltd – Business Card</title>
<link rel="stylesheet" href="https://fonts.googleapis.com/css2?family=Arimo:wght@400;700&family=Bitter:wght@400;500&display=swap">
<style>
  :root {
    --page-bg: #e9e7e4;
    --card-white: #ffffff;
    --brand-blue: #1d3ff2;
    --brand-dark: #2e2e30;
    --ink: #1c1c1c;
    --on-blue: #ffffff;
    --card-shadow: 0 6px 18px rgba(0,0,0,0.22);
  }
  * { margin: 0; padding: 0; box-sizing: border-box; }
  html, body {
    width: 1200px; height: 486px; overflow: hidden;
    background: var(--page-bg);
  }
  .stage {
    position: relative; width: 1200px; height: 486px;
    display: flex; justify-content: center; align-items: center; gap: 50px;
  }
  .card {
    position: relative; width: 540px; height: 320px;
    box-shadow: var(--card-shadow); overflow: hidden;
  }

  /* Front */
  .card--front { background: var(--card-white); color: var(--ink); }
  .edge-tab { position: absolute; left: 0; width: 9px; border-radius: 0 5px 5px 0; }
  .edge-tab--blue { top: 0; height: 150px; background: var(--brand-blue); }
  .edge-tab--dark { top: 168px; bottom: 0; background: var(--brand-dark); }
  .brand {
    position: absolute; left: 34px; top: 30px;
    display: flex; align-items: center; gap: 12px;
  }
  .brand__mark {
    width: 50px; height: 50px; border-radius: 50%;
    border: 6px solid var(--brand-blue); flex: none;
  }
  .brand__name {
    font-family: "Arimo", Arial, sans-serif; font-weight: 700;
    font-size: 22px; color: var(--brand-dark); letter-spacing: 0.2px;
  }
  .contact {
    position: absolute; right: 26px; top: 168px; text-align: right;
    font-family: "Bitter", Georgia, serif;
  }
  .contact__name { font-size: 22px; font-weight: 400; margin-bottom: 14px; }
  .contact__line {
    display: flex; justify-content: flex-end; align-items: center; gap: 7px;
    font-size: 14.5px; line-height: 1; margin-bottom: 11px;
  }
  .contact__line svg { width: 12px; height: 12px; flex: none; }

  /* Back */
  .card--back {
    background: var(--brand-blue); color: var(--on-blue);
    font-family: "Arimo", Arial, sans-serif; text-align: center;
  }
  .brand--back {
    position: static; justify-content: center; margin-top: 40px;
  }
  .brand--back .brand__mark { border-color: var(--on-blue); width: 58px; height: 58px; }
  .brand--back .brand__name { color: var(--on-blue); font-size: 24px; }
  .back__web { margin-top: 20px; font-size: 14px; font-weight: 700; letter-spacing: 0.3px; }
  .services__title { margin-top: 22px; font-size: 14px; font-weight: 700; }
  .services__rule {
    width: 170px; height: 1px; background: var(--on-blue);
    margin: 7px auto 10px;
  }
  .services__list { list-style: none; font-size: 14px; font-weight: 700; line-height: 20px; }
</style>
</head>
<body>
<main class="stage">
  <section class="card card--front" aria-label="Business card front">
    <span class="edge-tab edge-tab--blue"></span>
    <span class="edge-tab edge-tab--dark"></span>
    <div class="brand">
      <span class="brand__mark"></span>
      <span class="brand__name">Brivel Systems Group Ltd</span>
    </div>
    <div class="contact">
      <p class="contact__name">Morven Halsey</p>
      <p class="contact__line">
        <svg viewBox="0 0 24 24" aria-hidden="true"><path fill="#1c1c1c" d="M6.6 10.8a15 15 0 0 0 6.6 6.6l2.2-2.2c.3-.3.7-.4 1-.2 1.1.4 2.3.6 3.6.6.6 0 1 .4 1 1V20c0 .6-.4 1-1 1A17 17 0 0 1 3 4c0-.6.4-1 1-1h3.5c.6 0 1 .4 1 1 0 1.3.2 2.5.6 3.6.1.3 0 .7-.2 1z"/></svg>
        07845193870
      </p>
      <p class="contact__line">
        <svg viewBox="0 0 24 24" aria-hidden="true"><path fill="#1c1c1c" d="M2 6h20v12H2z"/><path fill="none" stroke="#fff" stroke-width="1.8" d="M2.5 6.5 12 13l9.5-6.5"/></svg>
        mhalsey@brivelsystems.co.uk
      </p>
      <p class="contact__line">
        <svg viewBox="0 0 24 24" aria-hidden="true"><circle cx="12" cy="12" r="10" fill="#1c1c1c"/><path fill="none" stroke="#fff" stroke-width="1.4" d="M2 12h20M12 2c3 3 3 17 0 20M12 2c-3 3-3 17 0 20"/></svg>
        www.brivelsystems.co.uk
      </p>
    </div>
  </section>

  <section class="card card--back" aria-label="Business card back">
    <div class="brand brand--back">
      <span class="brand__mark"></span>
      <span class="brand__name">Brivel Systems Group Ltd</span>
    </div>
    <p class="back__web">www.brivelsystems.co.uk</p>
    <p class="services__title">Our Services Include</p>
    <div class="services__rule"></div>
    <ul class="services__list">
      <li>• IT Infrastructure/Telephony Maintenance</li>
      <li>• Hosting Services</li>
      <li>• Kernix and Panora Solutions</li>
      <li>• App Development</li>
    </ul>
  </section>
</main>
</body>
</html>
```